Web Design Project

Current website needs stylish revamping www.trel-ika.com!!!! The look and font should be playful while showing maybe wings, shoes or something that is sexy yet confident for women to wear. The line is a division of a larger company and trademarked under their umbrella entity.

The website should have a clean, trendy and possibly modern look. Important project with hopeful long term business relation ship.

The slogan is also playful...
brr-ivo - made to glide, never pause
or
brr-ivo, quick in the stride (hence the idea of wings in the title or website)

brr-ivo...., shh, shoes be seen, not heard, light, ect.
Updates

Payment is now guaranteed- we appreciate your work!!!!

Would also like a possible slide show for the home page!!

Not many designs submitted!!! so design away - thank you greatly :)

Kindest regards,
NormaĀ 

Reason: need a great design for this project- appreciate your help!

Elegant sexy, not trashy!!!

also more clean, sophisticated and modern look- not too busy!!!
clients are high end
thank you so much!!
NormaĀ 

Target Market(s)

successful, working women

Industry/Entity Type

Business

Requirements
Must have
• Must be clean, buyer and user friendly and embody a sexy feel. Possibly bold colors or mix of neutral beige with black.

```html
<!DOCTYPE html>
<html lang="en">
<head>
<meta charset="utf-8">
<title>brr-ivo</title>
<link rel="stylesheet" href="https://fonts.googleapis.com/css2?family=Didact+Gothic&family=Montserrat:wght@400;600;700&family=Open+Sans+Condensed:wght@300;700&family=Arimo:wght@400;700&display=swap">
<style>
:root{
  --ink:#1a1a1a;
  --text:#333333;
  --muted:#555555;
  --nav:#5a5a5a;
  --nav-text:#ffffff;
  --panel:#eeeded;
  --line:#c9c9c9;
  --rule:#bdbdbd;
  --accent:#d0202a;
  --white:#ffffff;
  --btn:#4a4a4a;
}
*{box-sizing:border-box;margin:0;padding:0}
html,body{width:1200px;height:950px;overflow:hidden;background:var(--white)}
body{position:relative;font-family:"Didact Gothic",sans-serif;color:var(--text)}
a{color:inherit;text-decoration:none}
ul{list-style:none}

.site-header{position:absolute;left:0;top:0;width:1200px;height:100px;background:linear-gradient(#f7f7f7,#dcdcdc)}
.brand{position:absolute;left:48px;top:14px;font-family:"Didact Gothic",sans-serif;font-size:66px;line-height:70px;color:var(--ink);letter-spacing:-1px}
.account-links{position:absolute;right:44px;top:16px;display:flex;gap:8px;font-family:"Arimo",sans-serif;font-size:14px;color:var(--ink)}
.account-links span.sep{color:var(--ink)}
.search{position:absolute;left:650px;top:48px;width:507px;height:36px;border:1px solid var(--line);background:var(--white)}
.search-btn{position:absolute;right:0;top:0;width:40px;height:34px;border-left:1px solid var(--line);background:#f5f5f5;display:flex;align-items:center;justify-content:center}

.main-nav{position:absolute;left:0;top:100px;width:1200px;height:30px;background:var(--nav)}
.main-nav ul{display:flex;padding-left:44px;gap:0}
.main-nav li{font-family:"Montserrat",sans-serif;font-size:16.5px;line-height:30px;color:var(--nav-text);margin-right:39px;letter-spacing:.3px}

.promo-strip{position:absolute;left:44px;top:130px;width:1113px;height:64px;border-bottom:1px dotted var(--line);display:flex;align-items:center}
.promo{display:flex;align-items:center;gap:12px;font-size:16.5px;color:var(--muted)}
.promo strong{font-family:"Montserrat",sans-serif;font-weight:600;color:var(--text);font-size:16px}
.promo-gift{width:362px;padding-left:10px;border-right:1px solid var(--line);height:40px}
.promo-ship{width:382px;padding-left:50px;border-right:1px dotted var(--line);height:40px}
.promo-cart{padding-left:54px;height:40px}
.promo .count{color:var(--accent)}

.style-menu{position:absolute;left:44px;top:217px;width:248px;height:385px;background:var(--panel)}
.style-menu h2{margin:12px 0 0 12px;width:225px;height:27px;background:var(--ink);color:var(--white);font-family:"Montserrat",sans-serif;font-weight:400;font-size:16.5px;line-height:27px;padding-left:10px;letter-spacing:.5px}
.style-list{margin:0 12px;background:var(--white);padding:0 12px}
.style-list li{height:35px;line-height:36px;font-size:16.5px;color:var(--ink);border-bottom:1px dotted #aaaaaa;padding-left:6px}
.style-list li:last-child{border-bottom:none}
.newsletter{padding:12px 0 0 14px}
.newsletter .lead{display:block;font-family:"Open Sans Condensed",sans-serif;font-weight:300;font-size:32px;line-height:28px;color:var(--ink);letter-spacing:-.5px}
.newsletter .title{display:block;font-family:"Open Sans Condensed",sans-serif;font-weight:700;font-size:40px;line-height:40px;color:var(--ink);letter-spacing:.5px}
.email-field{margin-top:6px;width:218px;height:29px;border:1px solid var(--line);background:var(--white);font-size:14.5px;line-height:27px;padding-left:7px;color:var(--muted)}
.signup-btn{margin-top:13px;display:inline-block;width:78px;height:29px;border-radius:6px;background:var(--btn);color:var(--white);font-family:"Open Sans Condensed",sans-serif;font-weight:700;font-size:16px;line-height:29px;text-align:center}

.hero{position:absolute;left:316px;top:217px;width:841px;height:495px;background:
  radial-gradient(ellipse at 82% 30%,rgba(214,70,90,.55),transparent 40%),
  radial-gradient(ellipse at 60% 80%,#f1d9b4,transparent 60%),
  linear-gradient(100deg,#4a3530 0%,#6b4a3c 22%,#c59a78 45%,#ecd0a8 70%,#e8b9a0 100%)}

.footer-rule{position:absolute;left:44px;top:723px;width:1113px;height:5px;background:var(--rule)}
.site-footer{position:absolute;left:44px;top:736px;width:1113px;height:200px;display:flex;font-family:"Arimo",sans-serif}
.footer-col{border-right:1px solid var(--line);height:190px;padding-top:12px}
.footer-col:last-child{border-right:none}
.footer-col h3{font-size:15px;font-weight:700;color:var(--ink);letter-spacing:.3px;margin-bottom:8px}
.footer-col li{font-family:"Didact Gothic",sans-serif;font-size:15px;line-height:29px;color:var(--text)}
.col-help{width:164px}
.col-account{width:206px;padding-left:47px}
.col-looking{width:220px;padding-left:47px}
.col-companies{width:210px;padding-left:49px}
.col-follow{padding-left:48px}
.social{display:flex;gap:4px;margin:6px 0 14px}
.social span{width:25px;height:25px;display:block}
.social .s1{background:#4a66a0}
.social .s2{background:#4fb3e0}
.social .s3{background:#c8232c}
.social .s4{background:#b82520}
.social .s5{background:#cc1f1f;display:flex;align-items:center;justify-content:center}
.copyright{font-size:15px;line-height:18px;color:var(--ink);margin-bottom:8px}
.legal li{line-height:24px}
</style>
</head>
<body>

<header class="site-header">
  <div class="brand">brr-ivo</div>
  <nav class="account-links">
    <a href="#">My Account</a><span class="sep">/</span>
    <a href="#">Order Status</a><span class="sep">/</span>
    <a href="#">Wish Lists</a><span class="sep">/</span>
    <a href="#">Login</a><span class="sep">/</span>
    <a href="#">Register</a>
  </nav>
  <div class="search">
    <div class="search-btn">
      <svg width="20" height="20" viewBox="0 0 20 20"><circle cx="8" cy="8" r="6" fill="none" stroke="#333" stroke-width="2"/><line x1="12.5" y1="12.5" x2="18" y2="18" stroke="#333" stroke-width="2.5" stroke-linecap="round"/></svg>
    </div>
  </div>
</header>

<nav class="main-nav">
  <ul>
    <li>HOME</li><li>COLLECTIONS</li><li>NO MORE NOISE</li><li>ABOUT US</li><li>REVIEWS</li><li>BLOG</li><li>PRESS</li><li>STORES</li><li>CONTACT US</li>
  </ul>
</nav>

<section class="promo-strip">
  <div class="promo promo-gift">
    <svg width="44" height="44" viewBox="0 0 44 44"><rect x="6" y="18" width="32" height="24" fill="#c8343a"/><rect x="4" y="12" width="36" height="8" fill="#d94a4e"/><rect x="19" y="12" width="6" height="30" fill="#7bb342"/><path d="M22 12 C14 2 8 8 14 12 M22 12 C30 2 36 8 30 12" fill="none" stroke="#7bb342" stroke-width="3"/></svg>
    <span><strong>Buy Gift Cards</strong> Give The Perfect Gift</span>
  </div>
  <div class="promo promo-ship">
    <svg width="46" height="34" viewBox="0 0 46 34"><rect x="2" y="6" width="26" height="18" fill="#9fb6c9"/><path d="M28 12 H38 L44 19 V24 H28 Z" fill="#2f6fb5"/><circle cx="10" cy="27" r="4" fill="#333"/><circle cx="36" cy="27" r="4" fill="#333"/></svg>
    <span><strong>FREE</strong> Shipping and Returns</span>
  </div>
  <div class="promo promo-cart">
    <svg width="42" height="36" viewBox="0 0 42 36"><path d="M10 12 C12 2 30 2 32 12" fill="none" stroke="#9c1d1d" stroke-width="3"/><path d="M3 12 H39 L34 34 H8 Z" fill="#c22424"/><path d="M12 16 V30 M21 16 V30 M30 16 V30" stroke="#8a1515" stroke-width="2"/></svg>
    <span><strong>Shopping cart:</strong> <span class="count">0</span> items</span>
  </div>
</section>

<aside class="style-menu">
  <h2>CHOOSE BY STYLE</h2>
  <ul class="style-list">
    <li>Booties</li><li>Flats</li><li>Pumps</li><li>Slingbacks</li><li>View All</li>
  </ul>
  <div class="newsletter">
    <span class="lead">SIGN UP FOR OUR</span>
    <span class="title">NEWSLETTER</span>
    <div class="email-field">Your email address</div>
    <span class="signup-btn">SIGN UP</span>
  </div>
</aside>

<div class="hero" role="img" aria-label="Photo of a woman seated on a low ledge wearing dark high-heeled ankle booties, with a handbag beside her, warm blurred street behind"></div>

<div class="footer-rule"></div>
<footer class="site-footer">
  <div class="footer-col col-help">
    <h3>QUICK HELP</h3>
    <ul><li>Forgot Password?</li><li>Help Center</li><li>Community Forum</li><li>Contact Us</li><li>About Us</li></ul>
  </div>
  <div class="footer-col col-account">
    <h3>MY ACCOUNT</h3>
    <ul><li>Login/Register</li><li>My Cart</li><li>Buying Status</li><li>Watchlist</li><li>Dashboard</li></ul>
  </div>
  <div class="footer-col col-looking">
    <h3>LOOKING FOR?</h3>
    <ul><li>Stores</li><li>Free Classifieds</li><li>Advertising</li><li>Become an Affiliate</li><li>RSS Feeds</li></ul>
  </div>
  <div class="footer-col col-companies">
    <h3>COMPANIES</h3>
    <ul><li>CoinLeaf</li><li>Cartwell.com</li><li>Elmpost</li></ul>
  </div>
  <div class="footer-col col-follow">
    <h3>FOLLOW US</h3>
    <div class="social">
      <span class="s1"></span><span class="s2"></span><span class="s3"></span><span class="s4"></span>
      <span class="s5"><svg width="17" height="12" viewBox="0 0 17 12"><rect x=".75" y=".75" width="15.5" height="10.5" fill="none" stroke="#fff" stroke-width="1.5"/><path d="M1 1 L8.5 7 L16 1" fill="none" stroke="#fff" stroke-width="1.5"/></svg></span>
    </div>
    <p class="copyright">Copyright 2012 brrivo.<br>All rights reserved.</p>
    <ul class="legal"><li>Terms and Agreements</li><li>privacy policy</li></ul>
  </div>
</footer>

</body>
</html>
```